Hot sauce company needs a logo and label design- simple, clean & fresh

Wendel T's a hot pepper sauce company based on the edge of London needs a logo and label design .
The sauces are handmade in small batches with natural ingredients , no added sugars or extracts and so we would like a clean fresh label to reflect this - avoiding all the macho devil and flames novelty stuff.
At present there are four sauces - Jalapeno ,Chipotle,Habanero and Reaper we would like to have one Wendel T's label with the name of the sauce being changeable allowing us to react to what ingredients are available .
Updates

Project Deadline Extended
Reason: Hi Guys I have received a few requests to extend the deadline on the project and so I am thanks Wendel T's

Target Market(s)

people who care what they eat

Industry/Entity Type

Food Store

Logo Text

Wendel T's handmade hot sauce

Requirements
Must have
• Wendel T's handmade hot sauce - or the logo
• the name of the sauce ie jalapeno
• no added sugars
Nice to have
• handmade
• small batch
Should not have
• cartoon men with smoke coming out of their ears
• devils and the flames of hell

```html
<!DOCTYPE html>
<html lang="en">
<head>
<meta charset="UTF-8">
<title>Wendel T's Jalapeno Handmade Hot Sauce Label</title>
<link href="https://fonts.googleapis.com/css2?family=Special+Elite&family=Delius&display=swap" rel="stylesheet">
<style>
  :root {
    --ink: #111111;
    --chilli-red: #b01f24;
    --chilli-dark: #7e1418;
    --stem-green: #2a8a3a;
    --paper: #ffffff;
  }
  * { margin: 0; padding: 0; box-sizing: border-box; }
  html, body {
    width: 1200px;
    height: 892px;
    overflow: hidden;
    background: var(--paper);
  }
  .label {
    position: relative;
    width: 1200px;
    height: 892px;
    background: var(--paper);
    color: var(--ink);
  }
  .brand-name {
    position: absolute;
    left: 40px;
    top: 110px;
    width: 760px;
    text-align: center;
    font-family: "Special Elite", cursive;
    font-size: 118px;
    line-height: 1;
    color: var(--chilli-red);
  }
  .chilli-art {
    position: absolute;
    left: 210px;
    top: 320px;
    width: 400px;
    height: 180px;
    border-radius: 40px 120px 160px 60px;
    background: linear-gradient(160deg, var(--chilli-red) 0%, var(--chilli-red) 70%, var(--chilli-dark) 100%);
  }
  .sauce-name {
    position: absolute;
    left: 40px;
    top: 568px;
    width: 760px;
    text-align: center;
    font-family: "Special Elite", cursive;
    font-size: 76px;
    line-height: 1;
    letter-spacing: 2px;
  }
  .banner {
    position: absolute;
    left: 64px;
    top: 670px;
    width: 736px;
    height: 156px;
  }
  .banner svg { position: absolute; inset: 0; }
  .banner-text {
    position: absolute;
    left: 0;
    top: 52px;
    width: 100%;
    text-align: center;
    font-family: "Special Elite", cursive;
    font-size: 52px;
    line-height: 1;
  }
  .divider {
    position: absolute;
    left: 841px;
    top: 0;
    height: 892px;
    border-left: 5px dashed var(--ink);
  }
  .info {
    position: absolute;
    left: 876px;
    top: 62px;
    width: 316px;
    text-align: center;
  }
  .info-title {
    font-family: "Special Elite", cursive;
    font-size: 40px;
    font-weight: normal;
    line-height: 1;
  }
  .info-list {
    list-style: none;
    margin-top: 20px;
    padding-left: 14px;
    text-align: left;
    font-family: "Delius", cursive;
    font-size: 26px;
    line-height: 44px;
  }
  .info-copy {
    margin-top: 26px;
    font-family: "Delius", cursive;
    font-size: 25px;
    line-height: 37px;
  }
</style>
</head>
<body>
  <main class="label">
    <h1 class="brand-name">Wendel T's</h1>

    <div class="chilli-art" role="img" aria-label="Illustration of a red jalapeno chilli with a green stem"></div>

    <h2 class="sauce-name">JALAPENO</h2>

    <div class="banner">
      <svg viewBox="0 0 736 156" width="736" height="156" aria-hidden="true">
        <path d="M8 8 Q368 44 728 8 L700 78 L728 148 Q368 184 8 148 L36 78 Z"
              fill="#ffffff" stroke="#111111" stroke-width="5" stroke-linejoin="round"/>
      </svg>
      <p class="banner-text">HANDMADE HOT SAUCE</p>
    </div>

    <div class="divider"></div>

    <aside class="info">
      <h3 class="info-title">INGREDIENTS</h3>
      <ul class="info-list">
        <li>- no added sugars</li>
        <li>- handmade</li>
        <li>- small batch</li>
      </ul>
      <p class="info-copy">full of all the natural goodness of the earth with no added nasties, perfect with anything, May contain chilli and chilli products. good for all kinds of things including food, wash your hands after using and don't wipe your eyes with the same hand you are dipping in chilli sauce.</p>
    </aside>
  </main>
</body>
</html>
```